Corporate Design für Veranstalter von Fundraising-Events zum Thema Naturschutz
Zielgruppe
Wir sind eine Organisation, die Fundraising Events zum Thema Naturschutz organisiert. Spenden gehen an internationale Naturschutzprojekte. Unsere Zielgruppe sind große Firmen, wie auch private Spender von jung bis alt.
Aufgabenstellung
Wir suchen ein hochwertiges Design, das auf internationaler Bühne Zuspruch findet. Unternehmenssprache ist Englisch, daher bitte jeglichen Text in englischer Sprache verfassen. Der Name unser Organisation ist Colina Brava, was grüner Schmetterling in Spanisch bedeutet. Unser Logo sollte daher einen grünen Schmetterling enthalten und die Farbe Grün (hellgrün-saftig) die dominante Farbe im Corporate Design sein. Je nach Design könnten wir uns als weitere Farbakzente erdige Töne vorstellen, vorrangig orange.

```html
<!DOCTYPE html>
<html lang="en">
<head>
<meta charset="utf-8">
<title>Colina Brava – Letterhead</title>
<link rel="stylesheet" href="https://fonts.googleapis.com/css2?family=Arimo:wght@400;700&display=swap">
<style>
  :root {
    --green: #8cc04b;
    --ink: #1c1c1c;
    --dark: #333333;
    --paper: #ffffff;
    --mark: #555555;
  }
  html, body {
    margin: 0;
    padding: 0;
    overflow: hidden;
    background: var(--paper);
  }
  .letter {
    position: relative;
    width: 848px;
    height: 1200px;
    overflow: hidden;
    background: var(--paper);
    font-family: "Arimo", Arial, sans-serif;
    color: var(--ink);
  }
  .brand {
    position: absolute;
    top: 72px;
    left: 0;
    width: 848px;
    text-align: center;
    font-size: 50px;
    font-weight: 700;
    letter-spacing: 1px;
    color: var(--dark);
  }
  .brand-dot {
    display: inline-block;
    width: 18px;
    height: 18px;
    border-radius: 50%;
    background: var(--green);
    margin-right: 12px;
    vertical-align: middle;
  }
  .pattern {
    position: absolute;
    top: 26px;
    left: 694px;
    width: 140px;
    height: 156px;
    background: linear-gradient(135deg, rgba(140,192,75,0.15), rgba(140,192,75,0.55) 60%, rgba(51,51,51,0.25));
    border-radius: 4px;
  }
  .sender-line {
    position: absolute;
    top: 183px;
    left: 81px;
    font-size: 11px;
  }
  .fold-mark {
    position: absolute;
    left: 0;
    width: 21px;
    height: 1px;
    background: var(--mark);
  }
  .fold-mark.top { top: 423px; }
  .fold-mark.middle { top: 600px; }
  .fold-mark.bottom { top: 847px; }
  .recipient, .subject, .salutation, .body, .closing, .signature {
    position: absolute;
    left: 81px;
    margin: 0;
    font-size: 17px;
    line-height: 21px;
  }
  .recipient { top: 235px; }
  .subject { top: 419px; font-weight: 700; }
  .salutation { top: 483px; }
  .body { top: 541px; font-weight: 700; }
  .closing { top: 706px; }
  .signature { top: 748px; }
  .signature .org { color: var(--green); font-weight: 700; }
  .footer-rule {
    position: absolute;
    top: 1089px;
    left: 68px;
    width: 764px;
    height: 6px;
    background: var(--green);
  }
  .footer-col {
    position: absolute;
    top: 1112px;
    margin: 0;
    font-size: 13px;
    line-height: 17px;
    color: var(--ink);
  }
  .footer-col.address { left: 68px; }
  .footer-col.board { left: 325px; }
  .footer-col.bank { left: 631px; }
</style>
</head>
<body>
<main class="letter">
  <header>
    <div class="brand"><span class="brand-dot"></span>Colina Brava</div>
    <div class="pattern" role="img" aria-label="Decorative scatter of small green and dark leaves"></div>
    <div class="sender-line">Colina Brava - Lindenpfad 7 - 54321 Birkenau</div>
  </header>

  <span class="fold-mark top"></span>
  <span class="fold-mark middle"></span>
  <span class="fold-mark bottom"></span>

  <address class="recipient" style="font-style:normal">
    Tomas Feldberg<br>
    Lindenpfad 7<br>
    54321 Birkenau
  </address>

  <p class="subject">„Subject“</p>
  <p class="salutation">Dear Mr. Feldberg,</p>
  <p class="body">
    [Content]<br>[Content]<br>[Content]<br>[Content]<br>[Content]<br>[Content]
  </p>
  <p class="closing">Your's sincerely</p>
  <p class="signature">Ilse Wandrach<br><span class="org">Colina Brava</span></p>

  <footer>
    <div class="footer-rule"></div>
    <p class="footer-col address">Colina Brava<br>Lindenpfad 7<br>54321 Birkenau</p>
    <p class="footer-col board">Tomas Feldberg (1. Vorsitzender)<br>Carla Feldberg (2. Vorsitzende)<br>Ilse Wandrach (Schriftführerin)</p>
    <p class="footer-col bank">IBAN:DE987654321098765<br>BIC: COLBDE21<br>Reg. Nr.:87654321</p>
  </footer>
</main>
</body>
</html>
```